co working space / serviced office/ business centre

Brivlo - brivlo.in, is a very young brand bieng run by 3 young entrepreneurs. We want to be become out of the league company delivering fabulous and beautiful serviced offices in India and abroad. We hire designers who have made spaces across the world. We want to get visiting card design which gives complete fresh look to the people who carries that card, has to be very impactful and should symbolise happy young and energetic brand. should be completely out of the box thinking of international level, should portray global brand image.

Target Market(s)

Startups, (Small, medium and large corporates)

Industry/Entity Type

Business

Contact Information for Business Card

Name, Email, Address, Mobile number, Landline number, website

Colors

Designer to choose colors to be used in the design.

Requirements
Must have
• Nice new shape
Nice to have
• We want creative cuts, different size and impactful brand clarity
Should not have
• Boring and regular design and shape

```html
<!DOCTYPE html>
<html lang="en">
<head>
<meta charset="utf-8">
<title>Brivlo Business Card</title>
<link href="https://fonts.googleapis.com/css2?family=Open+Sans:wght@400;600;700&display=swap" rel="stylesheet">
<style>
  :root {
    --brand-red: #e8323c;
    --ink: #1a1a1a;
    --paper: #ffffff;
    --backdrop: #2e2e2e;
  }
  * { margin: 0; padding: 0; box-sizing: border-box; }
  html, body {
    width: 1200px; height: 864px; overflow: hidden;
    background: var(--backdrop);
    font-family: "Open Sans", sans-serif;
  }
  .stage {
    position: relative; width: 1200px; height: 864px;
  }
  .card {
    position: absolute; left: 290px;
    width: 620px; height: 354px;
    background: var(--paper);
    border-radius: 20px;
    overflow: hidden;
    box-shadow: 0 10px 30px rgba(0,0,0,.45);
  }
  .card-front { top: 50px; }
  .card-back { top: 454px; }

  .wordmark {
    display: flex; align-items: center; gap: 14px;
    color: var(--brand-red); font-weight: 700; letter-spacing: 2px;
    text-transform: uppercase;
  }
  .wordmark-dot {
    border-radius: 50%; background: var(--brand-red);
  }

  .front-mark {
    position: absolute; top: 110px; left: 0; right: 0;
    justify-content: center; font-size: 68px; line-height: 1;
  }
  .front-mark .wordmark-dot { width: 30px; height: 30px; }
  .front-url {
    position: absolute; top: 228px; left: 0; right: 0;
    text-align: center; font-size: 18px; color: var(--ink);
  }

  .back-swoosh { position: absolute; inset: 0; }
  .back-mark {
    position: absolute; top: 32px; right: 48px;
    font-size: 42px; line-height: 1; gap: 10px;
  }
  .back-mark .wordmark-dot { width: 20px; height: 20px; }

  .person { position: absolute; left: 60px; top: 178px; }
  .person-name { font-size: 23px; font-weight: 600; color: var(--ink); line-height: 1.2; }
  .person-role { font-size: 16px; color: var(--paper); line-height: 1.3; }

  .contacts {
    position: absolute; left: 62px; top: 246px;
    list-style: none; color: var(--paper); font-size: 15px;
  }
  .contacts li { display: flex; align-items: center; gap: 9px; line-height: 24px; }
  .contacts svg { width: 14px; height: 14px; flex: none; }

  .address {
    position: absolute; right: 44px; top: 232px;
    text-align: right; color: var(--paper); font-size: 14px; line-height: 1.45;
  }
</style>
</head>
<body>
<main class="stage">
  <section class="card card-front">
    <div class="wordmark front-mark"><span class="wordmark-dot"></span><span>Brivlo</span></div>
    <p class="front-url">www.brivlo.in</p>
  </section>

  <section class="card card-back">
    <svg class="back-swoosh" viewBox="0 0 620 354" preserveAspectRatio="none" aria-hidden="true">
      <path d="M0,196 Q250,120 620,104 L620,354 L0,354 Z" fill="var(--brand-red)"/>
      <path d="M210,152 Q420,98 620,84 L620,100 Q420,108 210,152 Z" fill="var(--ink)"/>
    </svg>

    <div class="wordmark back-mark"><span class="wordmark-dot"></span><span>Brivlo</span></div>

    <div class="person">
      <p class="person-name">John Smith</p>
      <p class="person-role">President</p>
    </div>

    <ul class="contacts">
      <li>
        <svg viewBox="0 0 16 16"><path fill="currentColor" d="M3.5 1.5l2.3 2.6-1.3 1.8c.9 2 2.5 3.6 4.5 4.5l1.8-1.3 2.6 2.3-1.4 2.1C7 12.8 3.2 9 2 3z"/></svg>
        <span>01 012-345-6789</span>
      </li>
      <li>
        <svg viewBox="0 0 16 16"><rect x="4" y="1" width="8" height="14" rx="1.5" fill="none" stroke="currentColor" stroke-width="1.6"/><circle cx="8" cy="12.5" r="0.9" fill="currentColor"/></svg>
        <span>01 012-345-6780</span>
      </li>
      <li>
        <svg viewBox="0 0 16 16"><rect x="1" y="3" width="14" height="10" fill="currentColor"/><path d="M1 3l7 6 7-6" fill="none" stroke="var(--brand-red)" stroke-width="1.4"/></svg>
        <span>info@yourwebsite.com</span>
      </li>
      <li>
        <svg viewBox="0 0 16 16"><g fill="none" stroke="currentColor" stroke-width="1.3"><circle cx="8" cy="8" r="6.5"/><ellipse cx="8" cy="8" rx="3" ry="6.5"/><path d="M1.5 8h13M2.5 4.8h11M2.5 11.2h11"/></g></svg>
        <span>www.brivlo.in</span>
      </li>
    </ul>

    <address class="address" style="font-style: normal;">
      Street Name, Suite 100<br>
      State, Zip Code, Country
    </address>
  </section>
</main>
</body>
</html>
```